Personal development products that change your life

This is a direct selling business that sells personal development courses, but also sells the business as well if desired. This is not MLM, and there is no handling of the product required, nor hassling friends or family. We are looking for business minded people wanting to work their own hours and achieve a desirable income from this. A success image or happy image on a flyer would be great. I'd like the website address to be displayed as well thanks. www.sunpath-growvista.com.au

Target Market(s)

Business-minded individuals searching for more finances. Self motivated, driven, interested in self development.

Industry/Entity Type

Business

Font styles to use
Sans Serif

Requirements
Must have
• Are you looking for
• - a franchise or business?
• - a change of career?
• - a back up income?
• Not MLM
• No product handling or shipping
• No hard sales required
• website: www.sunpath-growvista.com.au
Nice to have
• A picture or background of excited person jumping in the air, or some similar.
• Worded to enrol people interested in achieving more financial headway, or flexible hours, or travel and do this business from anywhere in the world.
• Only need access to a phone, internet connection and a desire to succeed.

```html
<!DOCTYPE html>
<html lang="en">
<head>
<meta charset="utf-8">
<title>Sunpath Growvista – Flyer</title>
<link href="https://fonts.googleapis.com/css2?family=Saira:ital,wght@1,800&family=Arimo:wght@400;700&family=Didact+Gothic&family=Oswald:wght@500&display=swap" rel="stylesheet">
<style>
  :root{
    --page:#e9e6e2;
    --navy-top:#24305f;
    --navy-mid:#3a4d9a;
    --orange:#e06a22;
    --orange-deep:#c85a16;
    --title-a:#f07a22;
    --title-b:#b5481a;
    --frame:#2c2d33;
    --stripe:#c9c9cc;
    --ink:#111111;
    --white:#ffffff;
    --band:#0d0d0d;
  }
  *{margin:0;padding:0;box-sizing:border-box}
  html,body{width:900px;height:1200px;overflow:hidden;background:var(--page)}
  .flyer{position:absolute;left:46px;top:28px;width:809px;height:1142px;overflow:hidden;
    box-shadow:0 6px 22px rgba(0,0,0,.35);font-family:'Arimo',Arial,sans-serif}
  .interior-photo{position:absolute;inset:0;
    background:linear-gradient(100deg,#d9dbdc 0%,#b9a892 30%,#8a7360 55%,#e7d6c3 80%,#f1e6da 100%)}
  .shapes{position:absolute;inset:0}
  .sky-photo{position:absolute;inset:0}
  .title{position:absolute;left:58px;top:40px;font-family:'Saira',sans-serif;font-style:italic;font-weight:800;
    font-size:60px;line-height:1;color:var(--title-a);letter-spacing:.5px}
  .subtitle{position:absolute;left:58px;top:112px;color:var(--white);font-weight:700;font-size:24px;line-height:29px}
  .checklist{position:absolute;left:0;top:342px;width:424px;height:255px;background:var(--orange);border-radius:0 6px 6px 0;color:var(--white)}
  .checklist h2{font-weight:700;font-size:33px;margin:32px 0 0 38px}
  .checklist ul{list-style:none;margin:16px 0 0 32px}
  .checklist li{font-family:'Didact Gothic',sans-serif;font-size:26px;height:45px;display:flex;align-items:center;gap:10px}
  .checklist svg{width:30px;height:30px;flex:none}
  .needs{position:absolute;left:0;top:632px;width:369px;height:200px;background:rgba(255,255,255,.55)}
  .needs p{margin:20px 0 0 31px;font-weight:700;font-size:24px;line-height:30px;color:var(--ink)}
  .perk{position:absolute;left:24px;height:45px;background:var(--orange);border-radius:0 6px 6px 0;color:var(--white);
    font-weight:700;font-size:23px;line-height:45px;padding-left:30px}
  .perk::before{content:"";position:absolute;left:-24px;top:0;width:20px;height:45px;background:var(--orange-deep);border-radius:0 4px 4px 0}
  .tagline{position:absolute;right:32px;top:912px;text-align:right;font-weight:700;font-size:34px;line-height:38px;color:var(--ink)}
  .footer-band{position:absolute;left:0;bottom:0;width:809px;height:50px;background:var(--band)}
  .url{position:absolute;left:281px;top:1052px;width:283px;height:60px;border-radius:10px;
    background:linear-gradient(#8a8a8a,#3d3d3d);color:var(--white);font-family:'Oswald',sans-serif;font-weight:500;
    font-size:19px;line-height:60px;text-align:center;letter-spacing:.3px}
</style>
</head>
<body>
<main class="flyer">
  <div class="interior-photo" role="img" aria-label="Softly blurred interior with hanging vintage filament light bulbs"></div>

  <svg class="shapes" width="809" height="1142" viewBox="0 0 809 1142" aria-hidden="true">
    <defs>
      <linearGradient id="navy" x1="0" y1="0" x2="0.6" y2="1">
        <stop offset="0" stop-color="var(--navy-top)"/>
        <stop offset="1" stop-color="var(--navy-mid)"/>
      </linearGradient>
    </defs>
    <polygon points="0,0 809,0 809,140 352,217 352,300 0,255" fill="url(#navy)"/>
    <polygon points="0,255 352,300 352,314 0,270" fill="var(--stripe)"/>
    <polygon points="352,217 809,140 809,805 694,893 352,852" fill="var(--frame)"/>
  </svg>

  <svg class="sky-photo" width="809" height="1142" viewBox="0 0 809 1142" role="img" aria-label="Three people jumping joyfully against a sunset sky, reflected in water">
    <defs>
      <linearGradient id="sky" x1="0" y1="0" x2="0" y2="1">
        <stop offset="0" stop-color="#5e7bb8"/>
        <stop offset=".35" stop-color="#c7b4b5"/>
        <stop offset=".5" stop-color="#2a2d44"/>
        <stop offset=".7" stop-color="#6a77a6"/>
        <stop offset="1" stop-color="#3b4269"/>
      </linearGradient>
    </defs>
    <polygon points="374,240 809,164 809,790 694,870 374,830" fill="url(#sky)"/>
  </svg>

  <h1 class="title">Sunpath Growvista</h1>
  <p class="subtitle">Ongoing personal development opportunities<br>for successful applicants</p>

  <section class="checklist">
    <h2>Are you looking for :</h2>
    <ul>
      <li><svg viewBox="0 0 30 30"><circle cx="15" cy="15" r="13" fill="none" stroke="#fff" stroke-width="2.5"/><path d="M9 15.5l4 4 8-9" fill="none" stroke="#fff" stroke-width="3" stroke-linecap="round" stroke-linejoin="round"/></svg>a franchise or business?</li>
      <li><svg viewBox="0 0 30 30"><circle cx="15" cy="15" r="13" fill="none" stroke="#fff" stroke-width="2.5"/><path d="M9 15.5l4 4 8-9" fill="none" stroke="#fff" stroke-width="3" stroke-linecap="round" stroke-linejoin="round"/></svg>a change of career?</li>
      <li><svg viewBox="0 0 30 30"><circle cx="15" cy="15" r="13" fill="none" stroke="#fff" stroke-width="2.5"/><path d="M9 15.5l4 4 8-9" fill="none" stroke="#fff" stroke-width="3" stroke-linecap="round" stroke-linejoin="round"/></svg>a back up income?</li>
    </ul>
  </section>

  <section class="needs">
    <p>All you need is<br>a laptop, a phone,<br>a strong desire<br>to succeed, and<br>dedicate 15-20<br>hours per week</p>
  </section>

  <div class="perk" style="top:864px;width:203px">Not MLM</div>
  <div class="perk" style="top:918px;width:333px">No hard sales required</div>
  <div class="perk" style="top:970px;width:445px">No product handling or shipping</div>

  <p class="tagline">Start the work /<br>life balance<br>you've always<br>wanted</p>

  <div class="footer-band"></div>
  <div class="url">WWW.SUNPATH-GROWVISTA.COM.AU</div>
</main>
</body>
</html>
```